Business Card For Life Coaching Business For Men

Take my existing logo and apply it to a business card. I would like the logo to be prominent with stylistic text below reading Life Coaching For Men. Contact info should show as:
Dale Hartwig
dale@steadforgepath.com

```html
<!DOCTYPE html>
<html lang="en">
<head>
<meta charset="utf-8">
<title>Steadforge Path – Business Card</title>
<link rel="stylesheet" href="https://fonts.googleapis.com/css2?family=Montserrat:wght@400;500;600;700;800&display=swap">
<style>
  :root {
    --navy: #2b2a8e;
    --navy-tint: #3a39a6;
    --teal: #0f8986;
    --ink: #1d1d2b;
    --paper: #ffffff;
    --backdrop: #e9e9ec;
  }
  * { box-sizing: border-box; margin: 0; padding: 0; }
  html, body {
    width: 1200px; height: 1186px; overflow: hidden;
    background: var(--backdrop);
    font-family: "Montserrat", sans-serif;
  }
  .canvas { position: relative; width: 1200px; height: 1186px; }
  .card {
    position: absolute; left: 160px; width: 880px; height: 503px;
    border-radius: 30px; overflow: hidden;
    box-shadow: 0 10px 30px rgba(0,0,0,.18);
  }
  .card--back { top: 60px; background: var(--navy); }
  .card--front { top: 623px; background: var(--paper); }

  /* back */
  .back-mark {
    position: absolute; left: 130px; top: 170px;
    display: flex; align-items: center; gap: 34px;
  }
  .back-mark__dot { width: 150px; height: 150px; border-radius: 50%; background: var(--navy-tint); }
  .back-mark__name {
    font-weight: 800; font-size: 64px; line-height: 1.02;
    color: var(--navy-tint); text-transform: uppercase; letter-spacing: 1px;
  }

  /* front */
  .brand {
    position: absolute; left: 60px; top: 188px;
    display: flex; align-items: center; gap: 18px;
  }
  .brand__dot { width: 90px; height: 90px; border-radius: 50%; background: var(--navy); flex: none; }
  .brand__text { display: flex; flex-direction: column; }
  .brand__name {
    font-weight: 800; font-size: 32px; line-height: 1.04;
    color: var(--navy); text-transform: uppercase;
  }
  .brand__tagline {
    margin-top: 10px;
    font-weight: 600; font-size: 12.5px; letter-spacing: 1.6px;
    color: var(--teal); text-transform: uppercase; white-space: nowrap;
  }
  .divider {
    position: absolute; left: 445px; top: 130px; width: 2px; height: 200px;
    background: var(--teal);
  }
  .person { position: absolute; left: 470px; top: 132px; }
  .person__name { font-weight: 800; font-size: 32px; color: var(--navy); }
  .person__title { font-size: 19px; color: var(--ink); margin-top: 2px; }
  .contacts { list-style: none; margin-top: 22px; }
  .contacts li {
    display: flex; align-items: center; gap: 12px;
    font-size: 19px; color: var(--ink); line-height: 1.55;
  }
  .contacts svg { width: 16px; height: 16px; flex: none; fill: var(--teal); }
  .address {
    position: absolute; left: 130px; top: 400px;
    font-size: 19px; color: var(--ink);
  }
  .bands { position: absolute; left: 0; top: 0; width: 880px; height: 503px; }
</style>
</head>
<body>
<div class="canvas">

  <section class="card card--back" aria-label="Card back">
    <div class="back-mark">
      <span class="back-mark__dot"></span>
      <span class="back-mark__name">Steadforge<br>Path</span>
    </div>
  </section>

  <section class="card card--front" aria-label="Card front">
    <svg class="bands" viewBox="0 0 880 503" aria-hidden="true">
      <polygon points="0,488 610,440 596,503 0,503" fill="var(--teal)"/>
      <polygon points="624,438 880,414 880,503 610,503" fill="var(--navy)"/>
    </svg>

    <div class="brand">
      <span class="brand__dot"></span>
      <div class="brand__text">
        <span class="brand__name">Steadforge<br>Path</span>
        <span class="brand__tagline">Life Coaching For Men</span>
      </div>
    </div>

    <div class="divider"></div>

    <div class="person">
      <h1 class="person__name">Dale Hartwig</h1>
      <p class="person__title">Managing Director</p>
      <ul class="contacts">
        <li>
          <svg viewBox="0 0 24 24"><path d="M6.6 10.8a15.1 15.1 0 0 0 6.6 6.6l2.2-2.2a1 1 0 0 1 1-.25 11.4 11.4 0 0 0 3.6.57 1 1 0 0 1 1 1V20a1 1 0 0 1-1 1A17 17 0 0 1 3 4a1 1 0 0 1 1-1h3.5a1 1 0 0 1 1 1c0 1.25.2 2.45.57 3.57a1 1 0 0 1-.25 1z"/></svg>
          555-014-0273
        </li>
        <li>
          <svg viewBox="0 0 24 24"><path d="M2 5h20v14H2z"/><path d="M3 6l9 7 9-7" fill="none" stroke="#fff" stroke-width="1.6"/></svg>
          dale@steadforgepath.com
        </li>
        <li>
          <svg viewBox="0 0 24 24"><circle cx="12" cy="12" r="10"/><path d="M2 12h20M12 2c3 3 3 17 0 20M12 2c-3 3-3 17 0 20" fill="none" stroke="#fff" stroke-width="1.4"/></svg>
          www.steadforgepath.com
        </li>
      </ul>
    </div>

    <p class="address">418 Birchline Ave, #112 Marlow Falls, OH 43019</p>
  </section>

</div>
</body>
</html>
```